Zelvana Advertising & Publicity business cards

I would like my Company's business card to be designed creatively & profissionally the logo is attached in both Arabic & english and prefer to have my emblem dimmed on the card as well
-Logo ( Arabic & English)
-Name (Arabic & English)
-Title ( Arabic & English)
-----------
-Location
-Landline (icon)
-Mobile phone (icon)
-Email (icon)
-Instagram (icon)
-WhatsApp (icon)

Target Market(s)

Industry/Entity Type

Marketing

Contact Information for Business Card

-Logo ( Arabic & English)
-Name (Arabic & English)
-----------
-Location
-Landline (icon)
-Mobile phone (icon)
-Email (icon)
-Instagram (icon)
-WhatsApp (icon)

Font styles to use
Serif

Requirements
Must have
• all what is mentions in business card details blanked and i will add the data my self
Nice to have
• Dim emblem on my business card both Arabic & english

```html
<!DOCTYPE html>
<html lang="en">
<head>
<meta charset="utf-8">
<title>Zelvana Advertising &amp; Publicity – Business Card</title>
<link rel="stylesheet" href="https://fonts.googleapis.com/css2?family=Questrial&family=Roboto+Condensed:wght@300;400&display=swap">
<style>
  :root {
    --canvas-grey: #e1e1e1;
    --paper-light: #f4f2ea;
    --teal: #44c2bf;
    --teal-glow: #86d3ce;
    --teal-mark: #3fc0bd;
    --ribbon: #6f6d73;
    --ribbon-fold: #4e4c52;
    --ink: #231f20;
    --white: #ffffff;
    --text-font: "Roboto Condensed", "Arial Narrow", sans-serif;
    --brand-font: "Questrial", "Century Gothic", sans-serif;
  }
  * { margin: 0; padding: 0; box-sizing: border-box; }
  html, body { width: 1200px; height: 702px; overflow: hidden; background: var(--canvas-grey); }
  .card {
    position: relative;
    width: 1200px;
    height: 702px;
    overflow: hidden;
    font-family: var(--text-font);
    background: linear-gradient(90deg, var(--canvas-grey) 0%, #ebebe6 55%, var(--paper-light) 100%);
  }
  .card-art { position: absolute; inset: 0; }

  .brand-mark { position: absolute; left: 102px; top: 319px; width: 74px; height: 74px; background: var(--teal-mark); }
  .brand-divider { position: absolute; left: 212px; top: 296px; width: 1.5px; height: 118px; background: var(--ink); }
  .brand-name, .brand-tagline {
    position: absolute; left: 229px; color: var(--ink);
    font-family: var(--brand-font); font-weight: 400; line-height: 1; white-space: nowrap;
  }
  .brand-name { top: 288px; font-size: 68px; }
  .brand-tagline { top: 382px; font-size: 22px; }

  .holder { position: absolute; right: 113px; top: 84px; text-align: right; font-weight: 300; }
  .holder-name { display: block; color: var(--white); font-size: 58px; line-height: 1; }
  .holder-title { display: block; color: var(--ink); font-size: 33px; line-height: 1; margin-top: 4px; }

  .contact { position: absolute; left: 665px; color: var(--white); font-weight: 300; line-height: 1; white-space: nowrap; }
  .contact-landline { top: 212px; font-size: 40px; }
  .contact-mobile { top: 292px; font-size: 40px; }
  .contact-email { top: 370px; font-size: 40px; }
  .contact-address { top: 452px; font-size: 34px; }
</style>
</head>
<body>
<div class="card">
  <svg class="card-art" width="1200" height="702" viewBox="0 0 1200 702" aria-hidden="true">
    <defs>
      <radialGradient id="panel-glow" cx="0.45" cy="0.45" r="0.7">
        <stop offset="0" stop-color="#86d3ce"/>
        <stop offset="1" stop-color="#44c2bf"/>
      </radialGradient>
    </defs>

    <rect class="contact-panel" x="571" y="0" width="554" height="702" fill="url(#panel-glow)"/>
    <rect class="side-strip" x="1125" y="0" width="75" height="702" fill="#e1e1e1"/>
    <rect class="name-tab" x="1105" y="80" width="20" height="73" fill="#6f6d73"/>

    <polygon class="ribbon-fold" points="558,265 571,265 571,274" fill="#4e4c52"/>
    <rect class="ribbon" x="558" y="199" width="567" height="66" fill="#6f6d73"/>
    <polygon class="ribbon-fold" points="1125,344 1139,344 1125,353" fill="#4e4c52"/>
    <rect class="ribbon" x="571" y="278" width="568" height="66" fill="#6f6d73"/>
    <polygon class="ribbon-fold" points="558,424 571,424 571,433" fill="#4e4c52"/>
    <rect class="ribbon" x="558" y="357" width="567" height="67" fill="#6f6d73"/>

    <g class="icon-landline" transform="translate(611 233)">
      <circle r="23" fill="none" stroke="#fff" stroke-width="2"/>
      <path d="M-9,-12 l5,-1 l4,8 l-4,3 q3,8 9,12 l3,-4 l8,4 l-1,5 q-3,3 -8,1 q-13,-6 -18,-20 q-1,-5 2,-8 z" fill="#fff"/>
    </g>
    <g class="icon-mobile" transform="translate(611 313)">
      <circle r="23" fill="none" stroke="#fff" stroke-width="2"/>
      <rect x="-8" y="-14" width="16" height="28" rx="2.5" fill="none" stroke="#fff" stroke-width="2"/>
      <line x1="-8" y1="8" x2="8" y2="8" stroke="#fff" stroke-width="1.5"/>
      <circle cy="11" r="1.3" fill="#fff"/>
    </g>
    <g class="icon-email" transform="translate(611 390)">
      <circle r="23" fill="none" stroke="#fff" stroke-width="2"/>
      <rect x="-12" y="-8" width="24" height="16" fill="#fff"/>
      <polyline points="-12,-8 0,2 12,-8" fill="none" stroke="#6f6d73" stroke-width="1.5"/>
    </g>
    <g class="icon-location" transform="translate(611 469)">
      <circle r="23" fill="none" stroke="#fff" stroke-width="2"/>
      <path d="M0,15 C-5,7 -10,1 -10,-4 A10,10 0 0 1 10,-4 C10,1 5,7 0,15 Z" fill="#fff"/>
      <circle cy="-4" r="4" fill="#44c2bf"/>
    </g>
    <circle class="icon-social" cx="611" cy="535" r="24" fill="#fff"/>
    <circle class="icon-social" cx="611" cy="599" r="24" fill="#fff"/>
  </svg>

  <span class="brand-mark"></span>
  <span class="brand-divider"></span>
  <span class="brand-name">Zelvana</span>
  <span class="brand-tagline">Advertising and Publicity</span>

  <div class="holder">
    <span class="holder-name">AlRashidi</span>
    <span class="holder-title">Job Title</span>
  </div>

  <div class="contact contact-landline">000.000.0000</div>
  <div class="contact contact-mobile">000.000.0000</div>
  <div class="contact contact-email">email@ email.com</div>
  <div class="contact contact-address">123 Address. City, State, Zip</div>
</div>
</body>
</html>
```